Private Investment Firm Needs PowerPoint Presentation Template

Design PowerPoint template, take Ridgeholm-submitted rough presentation draft, and drop it into new template. See attached Project Brief file for more detail.
Updates

Some decent designs have been submitted but they seem to lack the understanding of our target markets. I am hopeful that more time and feedback will result in better results.

Target Market(s)

Private company owners and intermediaries.

Font styles to use
Serif

Colors
3176b5

Requirements
Must have
• See attached Project Brief.
Nice to have
Should not have
• No B2C fluff--this is a B2B project.

```html
<!DOCTYPE html>
<html lang="en">
<head>
<meta charset="utf-8">
<title>Ridgeholm Capital – Non-Control Investor Questions</title>
<link rel="stylesheet" href="https://fonts.googleapis.com/css2?family=Lato:wght@400;700;900&family=Tinos:wght@400;700&display=swap">
<style>
:root{
  --navy:#1f3f5f;
  --blue:#3f7fc1;
  --blue-line:#3176b5;
  --teal:#1aa39a;
  --grey:#7a7a7a;
  --ink:#222;
  --white:#fff;
  --page-badge:#17a08f;
}
*{margin:0;padding:0;box-sizing:border-box}
html,body{width:1200px;height:334px;overflow:hidden;background:#fff}
.canvas{position:relative;width:1200px;height:334px;font-family:'Lato',Arial,sans-serif;color:var(--ink)}
.slide{position:absolute;top:0;height:334px;overflow:hidden;background:var(--white)}
.slide--questions{left:0;width:598px}
.slide--photo{left:600px;width:260px}
.slide--contact{left:860px;width:340px}

/* questions slide */
.section-tag{position:absolute;left:4px;top:24px;width:124px;height:26px}
.section-tag span{position:absolute;left:8px;top:6px;font-size:6.4px;font-weight:900;color:#fff;line-height:1.2;width:96px;text-align:center}
.slide-title{position:absolute;left:130px;top:6px;width:450px;text-align:center;font-weight:900;color:var(--navy);font-size:21px;line-height:1.12}
.band{position:absolute;left:4px;top:69px;width:592px;height:12px;background:var(--teal);color:#fff;font-size:7.4px;font-weight:900;text-align:center;line-height:12px}
.qa{position:absolute;left:8px;width:582px;display:flex;gap:2px}
.qa__question{width:208px;background:var(--blue);color:#fff;border-radius:4px;font-size:7.4px;line-height:1.18;padding:3px 8px;display:flex;align-items:center;text-align:center;justify-content:center}
.qa__question b{font-weight:900}
.qa__answer{flex:1;border:1.5px solid var(--blue-line);border-radius:4px;font-size:5.6px;line-height:1.22;padding:2px 10px;display:flex;flex-direction:column;justify-content:center}
.brand{position:absolute;display:flex;align-items:center;gap:3px;font-family:'Lato',Arial,sans-serif;font-weight:900;color:var(--navy);font-size:8px;letter-spacing:.5px}
.brand i{display:block;width:9px;height:9px;border-radius:50%;background:var(--navy)}
.page-no{position:absolute;width:17px;height:17px;border-radius:50%;background:var(--page-badge);color:#fff;font-size:7px;text-align:center;line-height:17px;border:2px solid #cfe9e5}

/* photo slide */
.photo-bg{position:absolute;inset:0;background:linear-gradient(135deg,#5a3f36 0%,#7d5a4b 35%,#a78a76 60%,#4a3a39 100%)}
.portrait-frame{position:absolute;left:56px;top:82px;width:172px;height:172px;background:#fff}
.portrait{position:absolute;left:24px;top:24px;width:128px;height:131px;background:linear-gradient(180deg,#c4ccd2,#56606e 70%,#2b3340)}

/* contact slide */
.contact-title{position:absolute;left:50px;top:14px;font-size:24px;font-weight:900;color:var(--navy);letter-spacing:.5px}
.contact-title span{color:var(--grey)}
.contact-item{position:absolute;left:60px;font-family:'Tinos','Times New Roman',serif;font-size:9.6px;line-height:13.4px;color:#555}
.contact-item strong{color:#111;font-size:10.4px}
.contact-item a{color:#1d52b0;text-decoration:underline}
.pin{position:absolute;left:58px;width:14px;height:18px}
.site{position:absolute;left:78px;top:295px;font-family:'Tinos','Times New Roman',serif;font-weight:700;font-size:11px;color:#111}
.search-icon{position:absolute;left:58px;top:292px;width:16px;height:16px}
</style>
</head>
<body>
<div class="canvas">

  <section class="slide slide--questions">
    <div class="section-tag">
      <svg width="124" height="26" viewBox="0 0 124 26"><polygon points="0,2 108,2 108,0 124,13 108,26 108,24 0,24" fill="#1aa39a"/></svg>
      <span>NON-CONTROL CAPITAL QUESTIONNAIRE</span>
    </div>
    <h1 class="slide-title">The Critical Questions to Ask of Any Prospective Non-Control Investor</h1>
    <div class="band">NON-CONTROL CAPITAL IS A SPECIALTY, SO ONLY THOSE FIRMS WITH DEEP EXPERIENCE INVESTING IT AS A TEAM SHOULD BE CONSIDERED</div>

    <div class="qa" style="top:90px;height:28px">
      <div class="qa__question"><p><b>Question #1:</b> How many years has the firm been investing Non-Control Capital?</p></div>
      <div class="qa__answer"><p>•Best Answer: 5+ years investing as a team within the current firm</p><p>•Indicates comfort and experience evaluating and making NCC investments with each other and increases likelihood of close</p></div>
    </div>
    <div class="qa" style="top:122px;height:28px">
      <div class="qa__question"><p><b>Question #2:</b> How may fully-invested Non-Control Capital funds in the firm's history?</p></div>
      <div class="qa__answer"><p>•Best Answer: 2+ fully-invested funds</p><p>•Indicates experience and ability to close deals with the current regime—those firms without it may only be testing the waters and not have a long-term commitment to NCC investing</p></div>
    </div>
    <div class="qa" style="top:154px;height:29px">
      <div class="qa__question"><p><b>Question #3:</b> What percentage of the firm's voting investment committee are full-time Non-Control Capital investors?</p></div>
      <div class="qa__answer"><p>•Best Answer: Super-majority</p><p>•Indicates commitment, experience, and focus on NCC and overcomes dependency on buyout heritage, if any</p></div>
    </div>
    <div class="qa" style="top:188px;height:30px">
      <div class="qa__question"><p><b>Question #4:</b> What is the number of Non-Control Capital investments made with the current firm and team?</p></div>
      <div class="qa__answer"><p>•Best Answer: 20+</p><p>•Indicates long-term experience and comfort with current team, investment committee, and NCC investment assessment</p></div>
    </div>
    <div class="qa" style="top:224px;height:29px">
      <div class="qa__question"><p><b>Question #5:</b> What percentage of portfolio investments made are "sponsorless" (those without a change-of-control investor)?:</p></div>
      <div class="qa__answer"><p>•Best Answer: 80%+ of all investments closed in the last 5 years (assumes current transaction is also sponsorless)</p><p>•Indicates ability to add-value as a sole minority investor and not simply as a back-up to another sponsor</p></div>
    </div>
    <div class="qa" style="top:258px;height:51px">
      <div class="qa__question"><p><b>Question #6:</b> Can the investor show quantifiable proof of their ability to assist portfolio companies with growth and improvement (assumes more than 20 exited Non-Control investments)?:</p></div>
      <div class="qa__answer"><p>•Best Answer: Yes (company owners should evaluate investors on actual historical revenue, EBITDA, and employee growth impact and the results should exceed what the current management has achieved on their own over the past 3 years)</p><p>•Indicates true value-added ability to help owners grow their businesses. Those without proof of their impact, or who are unwilling to disclose it, should be excluded</p></div>
    </div>

    <div class="brand" style="left:6px;top:316px"><i></i>RIDGEHOLM</div>
    <div class="page-no" style="left:556px;top:310px">19</div>
  </section>

  <section class="slide slide--photo">
    <div class="photo-bg" role="img" aria-label="Travel flat-lay with map, passport, sunglasses and plaid fabric"></div>
    <div class="portrait-frame">
      <div class="portrait" role="img" aria-label="Portrait of the firm's principal in a dark blazer"></div>
    </div>
    <div class="brand" style="left:6px;top:316px;color:#fff"><i style="background:#fff"></i>RIDGEHOLM</div>
  </section>

  <section class="slide slide--contact">
    <h2 class="contact-title">CONTACT <span>WITH US</span></h2>

    <svg class="pin" style="top:56px" viewBox="0 0 14 18"><path d="M7 1a6 6 0 0 0-6 6c0 4.5 6 10 6 10s6-5.5 6-10a6 6 0 0 0-6-6z" fill="none" stroke="#3176b5" stroke-width="1.8"/><circle cx="7" cy="7" r="2.2" fill="none" stroke="#3176b5" stroke-width="1.6"/></svg>
    <div class="contact-item" style="top:58px;left:78px">
      <strong>Daniel R. Whitmore</strong><br>Principal<br>41 Alder Ridge Road, Suite<br>210<br>Milford, CT 06460<br>Direct: (555) 214-0387<br><a>dwhitmore@ridgeholmcapital.com</a>
    </div>

    <svg class="pin" style="top:158px" viewBox="0 0 14 18"><path d="M7 1a6 6 0 0 0-6 6c0 4.5 6 10 6 10s6-5.5 6-10a6 6 0 0 0-6-6z" fill="none" stroke="#3176b5" stroke-width="1.8"/><circle cx="7" cy="7" r="2.2" fill="none" stroke="#3176b5" stroke-width="1.6"/></svg>
    <div class="contact-item" style="top:166px;left:78px">
      <strong>Boston Office</strong><br>18 Harbor View Drive, Suite 300<br>Salem, MA 01970<br>(555) 214-0300
    </div>

    <svg class="pin" style="top:225px" viewBox="0 0 14 18"><path d="M7 1a6 6 0 0 0-6 6c0 4.5 6 10 6 10s6-5.5 6-10a6 6 0 0 0-6-6z" fill="none" stroke="#3176b5" stroke-width="1.8"/><circle cx="7" cy="7" r="2.2" fill="none" stroke="#3176b5" stroke-width="1.6"/></svg>
    <div class="contact-item" style="top:232px;left:78px">
      <strong>San Francisco Office</strong><br>240 Market Lane, Suite 900<br>San Francisco, CA 94111<br>(555) 388-1400
    </div>

    <svg class="search-icon" viewBox="0 0 16 16"><circle cx="9.5" cy="6.5" r="4.8" fill="none" stroke="#3176b5" stroke-width="2"/><line x1="6" y1="10" x2="1.5" y2="14.5" stroke="#3176b5" stroke-width="2.4" stroke-linecap="round"/></svg>
    <div class="site">ridgeholmcapital.com</div>

    <div class="page-no" style="left:310px;top:303px">20</div>
  </section>

</div>
</body>
</html>
```